Real Estate - Car Wrap - Graphic design work for bus advertisement

Looking for graphic design work for Marcus Thornwell - Real Estate Associate. Name of the company is Thornwell Property Services. Slogan is:
Homes Made Simple Daily - We would really like to see the slogan used.

In need of an ad design that will be used for a bus ad. Bus ad specs included in attachments.

Bus ad info (Must include)
Marcus Thornwell
Keystar Summit logo
Marcus's phone number is 555-264-3817
Website is: Thornwellproperty.example
I have included the bus ad dimensions in the attachments

Our color scheme is Black & White with a hint of Navy Blue and we are open to a little bit of gold to add a little bit of color. We like the idea of the ad being in black and white and then just adding a hint of blue. Marcuss photo might be nice black and white. Open to ideas on this.

The final design should communicate professionalism, strength and approachability while being eye catching with a bit of wow factor. Something clean and modern with potentially some interesting graphic work.

Our ad design must incorporate the Keystar Summit Logo doesn't have to be in the color red like attached photo. It can be in any color that goes well with the ad just needs to be present.

We love the attached ad idea that I have included to help give some idea of where we are going. No purple however we want to stick with the Navy as the main color choice.

The dimensions for the bus ad are are attached in specs for the bus.
We really like the idea of using the head shot of Marcus standing in the blue shirt for the bus ad, (can be in color or black and white) We are however open to the other photo in attachments. Looking to see what you come up with.

I have included Marcus's name written in more of a signature font like the ad idea has. We want something in more of a signature for his name. See Signature for Marcus Thornwell for ex. Something as close to this as possible. Needs to be very easy to read from afar. Please don't include the strength of homes that is on this photo. We don't like this slogan.

I have attached, head shots of Marcus, Our companies current logo which is the house and an overall picture idea of the look we are going for. We really like this ad for an idea, black and white with a splash of color at the bottom. Again our color is Navy Blue.

Please message me if you have questions.
Thank you,

Lena Thornwell
Updates

Please note that Marcus’s photo needs to be on the business card. We also do not want any purple color in the design. The ad example image is just to give an idea of something we like. Thank you

Industry/Entity Type

Real Estate Agent

Font styles to use
Script

Requirements
Must have
• Colors are black and white with accent navy
Nice to have
• Open to a hint of gold
Should not have
• Any purple or light blue colors

```html
<!DOCTYPE html>
<html lang="en">
<head>
<meta charset="UTF-8">
<title>Marcus Thornwell – Bus Ad</title>
<link rel="stylesheet" href="https://fonts.googleapis.com/css2?family=Dancing+Script:wght@700&family=Ubuntu:ital,wght@0,500;0,700;1,500&display=swap">
<style>
  :root {
    --white: #ffffff;
    --band: #0e0f13;
    --navy: #2b2d6e;
    --navy-glow: #1c2a6a;
    --gold: #e0a53a;
    --ink: #111111;
    --photo-light: #d9d9d9;
    --photo-dark: #3a3a3a;
  }
  * { margin: 0; padding: 0; box-sizing: border-box; }
  html, body { width: 1200px; height: 559px; overflow: hidden; background: var(--white); }
  .ad {
    position: relative;
    width: 1200px;
    height: 559px;
    background: var(--white);
    overflow: hidden;
  }
  .agent-photo {
    position: absolute;
    left: 85px;
    top: 8px;
    width: 420px;
    height: 296px;
    background: radial-gradient(ellipse at 50% 30%, var(--photo-light) 0%, #9a9a9a 45%, var(--photo-dark) 100%);
    border-radius: 170px 170px 0 0;
  }
  .slogan {
    position: absolute;
    left: 600px;
    top: 110px;
    width: 560px;
    text-align: center;
    font-family: "Ubuntu", sans-serif;
    font-style: italic;
    font-weight: 500;
    font-size: 44px;
    color: var(--navy);
    white-space: nowrap;
  }
  .slogan-rule {
    position: absolute;
    left: 760px;
    top: 182px;
    width: 240px;
    height: 3px;
    background: var(--gold);
  }
  .info-band {
    position: absolute;
    left: 0;
    top: 304px;
    width: 1200px;
    height: 128px;
    background: var(--band);
  }
  .agent-name-plate {
    position: absolute;
    left: 48px;
    top: 322px;
    width: 480px;
    height: 104px;
    background: var(--navy-glow);
    border-radius: 18px;
    box-shadow: 0 0 18px 8px rgba(28, 42, 106, 0.85);
    display: flex;
    align-items: center;
    justify-content: center;
  }
  .agent-name {
    font-family: "Dancing Script", cursive;
    font-weight: 700;
    font-size: 60px;
    line-height: 1;
    color: var(--white);
    white-space: nowrap;
  }
  .website {
    position: absolute;
    left: 575px;
    top: 304px;
    width: 610px;
    height: 128px;
    display: flex;
    align-items: center;
    justify-content: center;
    font-family: "Ubuntu", sans-serif;
    font-weight: 700;
    font-size: 42px;
    color: var(--gold);
    white-space: nowrap;
  }
  .brand-block {
    position: absolute;
    left: 120px;
    top: 452px;
    width: 350px;
    display: flex;
    flex-direction: column;
    align-items: center;
    gap: 8px;
  }
  .company-name {
    display: flex;
    align-items: center;
    gap: 8px;
    font-family: "Ubuntu", sans-serif;
    font-weight: 500;
    font-size: 24px;
    color: var(--ink);
    white-space: nowrap;
  }
  .company-mark {
    width: 16px;
    height: 16px;
    background: var(--ink);
  }
  .brokerage-name {
    font-family: "Ubuntu", sans-serif;
    font-weight: 700;
    font-size: 34px;
    color: var(--ink);
    letter-spacing: 1px;
    white-space: nowrap;
  }
  .phone {
    position: absolute;
    left: 600px;
    top: 450px;
    width: 575px;
    height: 100px;
    display: flex;
    align-items: center;
    justify-content: center;
    font-family: "Ubuntu", sans-serif;
    font-weight: 700;
    font-size: 80px;
    color: var(--navy);
    letter-spacing: 1px;
    white-space: nowrap;
  }
</style>
</head>
<body>
  <main class="ad">
    <div class="agent-photo" role="img" aria-label="Black and white headshot of Marcus Thornwell in a dark suit"></div>
    <div class="slogan">Homes Made Simple Daily</div>
    <div class="slogan-rule"></div>
    <div class="info-band"></div>
    <div class="agent-name-plate">
      <span class="agent-name">Marcus Thornwell</span>
    </div>
    <div class="website">Thornwellproperty.example</div>
    <div class="brand-block">
      <div class="company-name"><span class="company-mark"></span>Thornwell Property Services</div>
      <div class="brokerage-name">Keystar Summit</div>
    </div>
    <div class="phone">555-264-3817</div>
  </main>
</body>
</html>
```